Web Design for New Antenna Company that is ready to revolutionize World Wide Communicaitons

This is the task description that I used for the Logo, please us it as a reference for the “message” of the company.

The name of the Company is "Verdant Arc Incorporated". We build highly efficient antennas that make a direct connection between communication points that make use of highly focus radio beams that support extremely high data rates (wireless internet) over the air.

The reference used for, antenna gain (the measure of an antennas' ability to focus/concentrate energy (radio energy) into a beam is measured by the antennas gain, which uses the Unit vAi, (decibels relative to an isotropic), and these are the initials of our corporate name. Antennas of high gain are focused like a laser, while the reference (isotropic) is a sphere or ball, radiating equally in all directions. The earth is a sphere. Think of Global Communications, as we will offer our products to all parts of the Globe, connecting people with vital information.

I like the feeling of "Direct" as it is definitive, and the idea of the "Beam" in that it carries information, so the main message is contained in the first two words "Verdant Arc" and Incorporated completes the idea and ties to the reference "vAi".

Our tag lines is: "Setting the standard for communications"

I have some 3D antenna patterns (shape of the energy in a 3 dimensional rendering). The colors that are chosen for the rainbow scale are, from most intense to lower intensity, red, sliding through orange to yellow, followed by green and then blue. I also like black for strong contrast. The radiated beam could be outlined in a strong color like black or blue, with a orange/red core color denoting temperature or intense heat (high energy / plasma). My thought of a logo would be a simple but strong image that somehow brings together the descriptions given above, possibly with a intense "beam" as described and possibly in the colors described, as long as the image does not get too "busy" or complex.

Don't feel confined by the use of any particular colors, just use your imagination and see if there is a simple strong image that brings the message home.

Thanks, I appreciate your ideas and look forward to seeing your work.

Regards,

Tam

I have files to share from the previous LOGO design, including EPS files for your use.

Thank you for your interest in providing a website for me.

Also find...

Please find the enclosed links to 3 website that I like, that are in my industry, which is Business to Business in Communications, both Government and Commercial.

Hopefully you can make use of reusing code, so please find something that fits the simple needs that I have.

The first looks too simple for me. The Graphics are too simple, with solid colors, and not too interesting.
http://pwaerials.example/

The second is Kellam Corporation is probably over the top, with the main graphics fanning out to each side. This is a nice effect, but not at all necessary.

I like to top “ribbon” selection” that open into outlined in solid color, filled rounded rectangles. It has a solid look. ( HOME COMPANY MARKETS/SOLUTIONS….)

I like the single page, with information on the bottom of the page, so you do not have to drill down to see what they are about.
http://kellam.example/

The following is probably the closest to what I may really need. This is smaller company, certainly smaller than Kellam, but not so personal as the smallest PW, that includes the designers resume.
http://www.mkfluxon.example/

I like the top of the site to resemble our Business Cards, Letterhead, showing our Logo with full Globe Background, (EPS file) which is enclosed in this mail.

I want to look like a serious company, displaying decades of experience, helping to build our Global Wireless communication system, that we all enjoy today.

I will be writing a Mission Statement, that will be included in the About US, or History Section. I would like to have an area for testimonials, as I have offers from some significant companies that would be happy to provide feedback on our design capabilities.

HOME About US, Markets/Solutions Products/Services

I like that the areas above, when hovered show the pull down without having to actually select the item.

I will enclose, if you send me your e-mail the files to assist... "my favorite" is the Logo, that I like best. I think that the lines and continents on the Globe need to be brought out better so they can be seen. I am including the source files (.eps & .rar)

I will be glad to include other JPEGs of logos that are of different colors on white background. The "tag line" under the name should always be "Setting the Standard for Communications" and not "We set..."

Thanks for your help. I look forward to your proposals Please do not hesitate to call.

Regards,

Tam

Cell # 555-271-9034
tamholt@verdantarcinc.example

I do have files (eps, rar) files for the logo design that I would like used in the website.
Please send an e-mail request at: tamholt@verdantarcinc.example and I will forward them to you.

I can also send you the brief, that was used for the LOGO request, that may provide insight to
the type of message that I want to convey.

Thanks,

Tam

Reason: I am extending to allow enough time so that we are not rushed.

```html
<!DOCTYPE html>
<html lang="en">
<head>
<meta charset="utf-8">
<title>Verdant Arc Incorporated</title>
<link href="https://fonts.googleapis.com/css2?family=Hind:wght@300;400;500;600;700&family=Roboto:wght@400&display=swap" rel="stylesheet">
<style>
:root{
  --page:#f4f5f7;
  --ink:#222;
  --grey:#777;
  --mid:#8a8a8a;
  --navy:#1f3f92;
  --navy-dark:#183380;
  --cyan:#1a9fdc;
  --cyan-light:#2fb4ea;
  --link:#1d4aa0;
  --hero:#2a2a2a;
  --footer:#1d1d1d;
  --footer-text:#9a9a9a;
  --rule:#dcdcdc;
}
*{margin:0;padding:0;box-sizing:border-box}
html,body{width:1200px;height:977px;overflow:hidden}
body{background:radial-gradient(ellipse at 50% 30%,#fff 0%,#fbfbfc 45%,var(--page) 100%);font-family:"Hind",sans-serif;color:var(--ink);position:relative}
.abs{position:absolute}

/* header */
.brand{left:190px;top:22px;display:flex;align-items:center;gap:10px}
.brand-dot{width:40px;height:40px;border-radius:50%;background:var(--navy)}
.brand-name{font-size:20px;font-weight:600;color:var(--navy);line-height:1}
.phone{right:190px;top:10px;font-size:25px;color:var(--ink);display:flex;align-items:center;gap:6px;font-weight:400}
.search{left:570px;top:54px;width:276px;height:32px;border:1px solid #cfcfcf;background:#f3f3f3;border-radius:2px}
.search span{position:absolute;left:8px;top:8px;font-size:11px;color:#aaa}
.search svg{position:absolute;right:6px;top:3px}
.account{left:870px;top:52px;font-size:13px;color:var(--grey);line-height:18px}
.account a,.cart a{color:var(--link);text-decoration:none}
.account .sep{color:#bbb;margin:0 5px}
.cart{left:975px;top:52px;font-size:13px;color:var(--grey);line-height:18px}
.vsep{top:54px;width:1px;height:32px;background:#ddd}

/* nav */
.nav-rule{left:190px;top:102px;width:820px;height:1px;background:#e3e3e3}
.nav{left:190px;top:114px;display:flex;font-size:14.5px;color:#666;font-weight:400}
.nav span{padding:0 19px;border-left:1px solid #dcdcdc;line-height:22px}
.nav span:first-child{padding-left:0;border-left:none}
.social{left:894px;top:113px;display:flex;gap:6px}
.social i{width:24px;height:24px;border-radius:50%;background:#111;display:block}

/* product sidebar */
.sidebar{left:190px;top:148px;width:208px;height:259px;background:linear-gradient(180deg,var(--cyan-light) 0%,var(--cyan) 30%,#1c6fbf 70%,var(--navy) 100%)}
.sidebar h2{font-size:24px;font-weight:700;color:#fff;padding:3px 10px 0;height:38px;border-bottom:2px solid rgba(0,0,0,.15)}
.sidebar ul{list-style:none;margin-top:6px}
.sidebar li{font-size:13px;color:#fff;padding:0 12px;height:25.6px;line-height:27px;border-bottom:1px solid rgba(255,255,255,.12)}
.sidebar li:last-child{border-bottom:none}

/* hero */
.hero{left:402px;top:148px;width:608px;height:259px;background:linear-gradient(180deg,#333 0%,var(--hero) 100%);overflow:hidden}
.hero-art{position:absolute;right:10px;top:0;width:250px;height:259px;background:radial-gradient(ellipse at 60% 45%,#e6e6e6 0%,#bdbdbd 45%,#3a3a3a 75%,transparent 80%)}
.hero h1{position:absolute;left:22px;top:8px;font-size:84px;font-weight:700;letter-spacing:-3px;line-height:1;background:linear-gradient(180deg,#fff 0%,#9a9a9a 55%,#e0e0e0 100%);-webkit-background-clip:text;background-clip:text;color:transparent}
.hero .sub{position:absolute;left:24px;top:80px;font-size:43px;color:#fff;font-weight:400;line-height:1}
.hero .sub em{font-style:normal;color:var(--cyan-light)}
.hero p{position:absolute;left:28px;top:126px;width:310px;font-size:11px;line-height:16px;color:#c9c9c9;font-weight:300}
.btn{display:inline-block;background:linear-gradient(180deg,var(--cyan-light),var(--cyan));color:#fff;font-size:14px;font-weight:500;border:1px solid #7fd0f3;border-radius:2px;padding:5px 8px 2px;line-height:20px}
.hero .btn{position:absolute;left:28px;top:206px}
.dots{position:absolute;right:10px;bottom:10px;display:flex;gap:5px}
.dots i{width:12px;height:12px;border-radius:50%;border:1.5px solid #ddd;display:block}
.dots i.on{background:var(--cyan);border-color:var(--cyan-light)}

/* welcome */
.welcome{left:190px;top:422px;font-size:39px;color:var(--mid);font-weight:400}
.welcome b{color:#111;font-weight:700}
.intro{left:190px;top:472px;width:820px;font-family:"Roboto",sans-serif;font-size:9.6px;line-height:14.4px;color:#888}
.intro-btn{left:190px;top:528px}
.divider{left:190px;top:584px;width:820px;height:1px;background:var(--rule)}

/* features */
.features-title{left:189px;top:601px;font-size:25px;color:#222;font-weight:400}
.card{top:642px;width:268px;height:142px;overflow:visible}
.card .map{position:absolute;inset:0}
.card .art{position:absolute;right:14px;top:-10px;width:96px;height:152px;border-radius:4px}
.card h3{position:absolute;left:11px;top:10px;color:#fff;font-weight:500;line-height:1}
.card h3 .code{display:block;font-size:20px;letter-spacing:-.5px}
.card h3 .kind{display:block;font-size:31px;margin-top:1px}
.card .cart-btn{position:absolute;left:11px;top:104px;font-size:13px;padding:4px 6px 1px;border-radius:2px;line-height:20px}
.card.navy .map{background:radial-gradient(ellipse at 40% 60%,#2a55aa 0%,var(--navy) 60%,var(--navy-dark) 100%)}
.card.cyan .map{background:radial-gradient(ellipse at 40% 60%,#35b6ec 0%,var(--cyan) 65%,#1590cc 100%)}
.card.navy .cart-btn{background:#f2f4f8;color:var(--navy)}
.card.cyan .cart-btn{background:#1b1b1b;color:#fff}
.art.dish{background:linear-gradient(160deg,#f3f3f3 0%,#b9b9b9 55%,rgba(60,60,60,.5) 100%)}
.art.tower{background:linear-gradient(180deg,rgba(255,255,255,.35) 0%,rgba(220,220,220,.55) 100%)}
.art.sat{background:linear-gradient(160deg,#e9e9e9 0%,#777 50%,#dcdcdc 100%)}

/* footer */
.footer{left:190px;top:808px;width:820px;height:169px;background:var(--footer)}
.fcol{position:absolute;top:10px}
.fcol h4{color:#fff;font-size:15px;font-weight:500;margin-bottom:6px}
.fcol li{list-style:none;font-size:10.5px;color:var(--footer-text);line-height:18.5px;font-weight:300}
.news{left:525px;width:280px}
.news-item{display:flex;gap:8px;padding:2px 0 7px 5px;border-bottom:1px solid #333;margin-bottom:7px}
.news-date{font-size:10px;color:#888;text-align:center;line-height:12px;padding-top:1px}
.news-text{font-size:10.5px;color:var(--footer-text);line-height:13.5px;font-weight:300}
.news-text b{color:#fff;font-weight:400}
.copy{position:absolute;left:0;bottom:0;width:820px;height:32px;border-top:1px solid #2c2c2c;text-align:center;font-size:9.5px;color:#666;line-height:32px;font-weight:300}
</style>
</head>
<body>

<header>
  <div class="abs brand"><i class="brand-dot"></i><span class="brand-name">Verdant Arc Incorporated</span></div>
  <div class="abs phone">
    <svg width="18" height="18" viewBox="0 0 24 24"><path fill="#222" d="M6.6 10.8a15.2 15.2 0 0 0 6.6 6.6l2.2-2.2c.3-.3.7-.4 1-.2 1.1.4 2.3.6 3.6.6.6 0 1 .4 1 1V20c0 .6-.4 1-1 1A17 17 0 0 1 3 4c0-.6.4-1 1-1h3.5c.6 0 1 .4 1 1 0 1.3.2 2.5.6 3.6.1.3 0 .7-.2 1z"/></svg>
    555-318-4402
  </div>
  <div class="abs search"><span>Search...</span>
    <svg width="26" height="26" viewBox="0 0 26 26"><circle cx="10.5" cy="10.5" r="7" fill="none" stroke="#1a8fd0" stroke-width="3"/><line x1="15.5" y1="15.5" x2="23" y2="23" stroke="#1a8fd0" stroke-width="4" stroke-linecap="round"/></svg>
  </div>
  <div class="abs vsep" style="left:858px"></div>
  <div class="abs account">Hello!<br><a>Login</a><span class="sep">|</span><a>SignUp</a></div>
  <div class="abs vsep" style="left:962px"></div>
  <div class="abs cart">Cart<br><a>0 Item</a></div>
</header>

<div class="abs nav-rule"></div>
<nav class="abs nav"><span>Home</span><span>About Us</span><span>Markets/Solutions</span><span>Products/Services</span><span>Contact Us</span></nav>
<div class="abs social"><i></i><i></i><i></i><i></i></div>

<aside class="abs sidebar">
  <h2>Products</h2>
  <ul>
    <li>Accessories</li><li>Antennas</li><li>Broadband</li><li>Combiners</li>
    <li>Duplexers</li><li>Radio Energy</li><li>Tower Top Amplifiers</li><li>Wireless Internet</li>
  </ul>
</aside>

<section class="abs hero">
  <div class="hero-art" role="img" aria-label="Large white satellite dish antenna"></div>
  <h1>SETTING</h1>
  <div class="sub">the <em>standard</em> for</div>
  <p>We build highly efficient antennas that make a direct connection between communication points that make use of highly focus radio beams that support extremely high data rates (wireless internet) over the air.</p>
  <span class="btn">Learn More</span>
  <div class="dots"><i class="on"></i><i></i><i></i><i></i></div>
</section>

<h2 class="abs welcome">Welcome to <b>vAi</b></h2>
<p class="abs intro">Lorem ipsum dolor sit amet, consectetur adipiscing elit. Mauris at facilisis magna. Suspendisse cursus augue sit amet scelerisque bibendum. Integer arcu sem, auctor sit amet sagittis in, dapibus eu purus. Vivamus elementum semper risus, quis pellentesque libero accumsan id. Proin placerat fermentum lacus. Etiam dolor nibh, fermentum nec vehicula a, vestibulum id metus. Aliquam erat volutpat. Donec interdum a magna vitae aliquet. Phasellus ut tempor justo. Fusce nisi nibh, luctus sed placerat eget, fringilla in erat</p>
<span class="abs btn intro-btn">Learn More</span>
<div class="abs divider"></div>

<h2 class="abs features-title">Feature Products</h2>

<article class="abs card navy" style="left:190px">
  <div class="map" role="img" aria-label="Faint world map background"></div>
  <div class="art dish" role="img" aria-label="Satellite dish on a lattice mount"></div>
  <h3><span class="code">KRT-518PLM</span><span class="kind">Antenna</span></h3>
  <span class="cart-btn">Add to Cart</span>
</article>
<article class="abs card cyan" style="left:466px">
  <div class="map" role="img" aria-label="Faint world map background"></div>
  <div class="art tower" role="img" aria-label="Radio tower emitting signal rings"></div>
  <h3><span class="code">KRT-903TNX</span><span class="kind">Antenna</span></h3>
  <span class="cart-btn">Add to Cart</span>
</article>
<article class="abs card navy" style="left:742px">
  <div class="map" role="img" aria-label="Faint world map background"></div>
  <div class="art sat" role="img" aria-label="Satellite with solar panels"></div>
  <h3><span class="code">KRT-471836</span><span class="kind">Antenna</span></h3>
  <span class="cart-btn">Add to Cart</span>
</article>

<footer class="abs footer">
  <div class="fcol" style="left:13px"><h4>Navigation</h4><ul><li>Home</li><li>About Us</li><li>Markets/Solutions</li><li>Products/Services</li></ul></div>
  <div class="fcol" style="left:183px"><h4>Products</h4><ul><li>Antennas</li><li>Radio Energy</li><li>Tower Top Amplifiers</li><li>Wireless Internet</li></ul></div>
  <div class="fcol" style="left:364px"><h4>Customers</h4><ul><li>Contact Us</li><li>Customer Log-in</li><li>Training/Support</li></ul></div>
  <div class="fcol news"><h4>News</h4>
    <div class="news-item"><div class="news-date">OCT<br>30</div><div class="news-text">Lorem ipsum dolor sit amet, consectetur adipiscing elit. Morbi in gravida orci. <b>Read More</b></div></div>
    <div class="news-item"><div class="news-date">OCT<br>31</div><div class="news-text">Lorem ipsum dolor sit amet, consectetur adipiscing elit. Morbi in gravida orci. <b>Read More</b></div></div>
  </div>
  <div class="copy">Copyright © 2013 www.verdantarcinc.example &nbsp;|&nbsp; All rights reserved &nbsp;|&nbsp; Terms &amp; Conditions &nbsp;|&nbsp; Privacy Policy</div>
</footer>

</body>
</html>
```